Stationery for Heating Plumbing & Electrical Contractor
Veltrana
Stationery for Heating Plumbing & Electrical Contractor - Construction
Creative Brief
Professional
Neil Farrow
Director
428b Pellham Rd , Oakvane, Warrington , Cheshire QX7 3PZ
Mornwick@fenmail.com
www.veltrana.uk.com

```html
<!DOCTYPE html>
<html lang="en">
<head>
<meta charset="utf-8">
<title>Veltrana – Business Card</title>
<link href="https://fonts.googleapis.com/css2?family=Open+Sans:wght@300;400;600;700&display=swap" rel="stylesheet">
<style>
  :root {
    --backdrop: #e9e9ea;
    --card-dark: #3b3b3d;
    --card-darker: #2e2e30;
    --rim-orange: #f38a1f;
    --rim-silver: #c9cacc;
    --text-light: #ffffff;
    --text-muted: #d9d9da;
    --accent: #f5a126;
  }
  * { box-sizing: border-box; margin: 0; padding: 0; }
  html, body {
    width: 1200px; height: 900px; overflow: hidden;
    background: var(--backdrop);
    font-family: "Open Sans", Arial, sans-serif;
  }
  .canvas {
    width: 1200px; height: 900px;
    display: flex; align-items: center; justify-content: center;
  }
  .card {
    width: 920px; height: 540px;
    border-radius: 240px / 230px;
    background: var(--rim-orange);
    padding: 14px;
  }
  .card-rim {
    width: 100%; height: 100%;
    border-radius: 228px / 218px;
    background: var(--rim-silver);
    padding: 5px;
  }
  .card-face {
    position: relative;
    width: 100%; height: 100%;
    border-radius: 224px / 214px;
    background: radial-gradient(ellipse at 50% 35%, var(--card-dark) 0%, var(--card-darker) 100%);
    color: var(--text-light);
  }
  .brand {
    position: absolute; left: 0; right: 0; top: 88px;
    display: flex; align-items: center; justify-content: center; gap: 22px;
  }
  .brand-dot {
    width: 96px; height: 96px; border-radius: 50%;
    background: var(--accent);
  }
  .brand-name {
    font-size: 64px; font-weight: 300; letter-spacing: 1px;
    color: var(--text-light);
  }
  .person {
    position: absolute; left: 0; right: 0; top: 238px;
    text-align: center;
  }
  .person-name {
    font-size: 34px; font-weight: 700; letter-spacing: 1px;
    text-transform: uppercase;
  }
  .person-role {
    font-size: 21px; font-weight: 400; color: var(--text-muted);
    margin-top: 2px;
  }
  .contact {
    position: absolute; right: 118px; top: 360px;
    font-size: 17px; color: var(--text-light);
    display: flex; flex-direction: column; gap: 6px;
  }
  .contact-email { padding-left: 60px; }
  .contact-line { display: flex; align-items: center; gap: 6px; }
  .contact-icon { width: 14px; height: 14px; flex: none; }
  .contact-sep { margin-left: 8px; }
</style>
</head>
<body>
<main class="canvas">
  <article class="card">
    <div class="card-rim">
      <div class="card-face">
        <header class="brand">
          <span class="brand-dot"></span>
          <span class="brand-name">veltrana</span>
        </header>

        <section class="person">
          <h1 class="person-name">Neil Farrow</h1>
          <p class="person-role">Managing Director</p>
        </section>

        <address class="contact" style="font-style:normal">
          <span class="contact-email">Mornwick@fenmail.com</span>
          <span class="contact-line">
            <svg class="contact-icon" viewBox="0 0 14 14"><path d="M7 1a4 4 0 0 0-4 4c0 3 4 8 4 8s4-5 4-8a4 4 0 0 0-4-4z" fill="#fff"/><circle cx="7" cy="5" r="1.5" fill="#333"/></svg>
            428b Pellham Rd , Oakvane
          </span>
          <span class="contact-line">
            <svg class="contact-icon" viewBox="0 0 14 14"><path d="M3 1l2.5 0 1 3-1.5 1.2a7 7 0 0 0 3.8 3.8L10 7.5l3 1V11a1.5 1.5 0 0 1-1.5 1.5A10.5 10.5 0 0 1 1.5 2.5 1.5 1.5 0 0 1 3 1z" fill="#fff"/></svg>
            014 582 3076
            <svg class="contact-icon contact-sep" viewBox="0 0 14 14"><circle cx="7" cy="7" r="6" fill="none" stroke="#fff" stroke-width="1.4"/><path d="M1 7h12M7 1c-2.5 3-2.5 9 0 12M7 1c2.5 3 2.5 9 0 12" fill="none" stroke="#fff" stroke-width="1.1"/></svg>
            www.veltrana.uk.com
          </span>
        </address>
      </div>
    </div>
  </article>
</main>
</body>
</html>
```